Scrum Master & Agile IT Coach Needing Business Website

Hello, my name is Brent Holloway
I am a project manger, scrum master, & agile coach. I work with IT development teams on major projects for Fortune 500 companies . My project management business has a website and can be found here: www.tq-keystride.example

I have launched a new company, ALL focused on IT Agile Coaching, I am looking to have a website created for my new company - the name of the new company is: Pins and Dials - Agile IT Coaching and Training.
I have a logo and it is provided in the materials. I like to logo; I am open to different color pallets.

The website will have a total of 7 pages; I have content for 5 of the 7 pages prepared; the other 2 pages will say under construction.

Page 1 Who am I, What I do, My Experience
Demonstrated experience and progression from Scrum Master to
Program Manager to Coach

Page 2 Pins & Dials - Agile Team Coaching
teams working major IT projects, multiple months/years

Page 3 Coaching @ the Team Level

Page 4 Coaching @ the Program Level ; LYNQ BQR level

Pages 5 -6 Under Construction

Page 7 Presentations, Slide Decks, Reference Materials

Mentor Nook need to have this highlighted somewhere Monthly Blog
Updates

Industry/Entity Type

IT development

Coding

Coded - Design and coding required

Number of Pages Required

5+ page

Requirements
Must have
• the website must be bold - I want those who visit to remember coming to my coaching site
Nice to have
• nice to have will be a modern / futuristic website; I work with IT developers, I want a website they will like
Should not have
• should not be stiff - it should be professional but fun

```html
<!DOCTYPE html>
<html lang="en">
<head>
<meta charset="utf-8">
<title>Pins &amp; Dials - Agile Team Coaching</title>
<link href="https://fonts.googleapis.com/css2?family=Roboto:wght@400;500;700;900&family=Open+Sans:wght@400;600;700&display=swap" rel="stylesheet">
<style>
:root{
  --white:#ffffff;
  --sky:#75a8d8;
  --blue:#4689c8;
  --ink-blue:#3a76b4;
  --navy:#0d2551;
  --navy-faint:#2a4470;
  --text:#1d1d1d;
  --bar:#333333;
  --photo-a:#cfc6bd;
  --photo-b:#6d7480;
}
*{box-sizing:border-box;margin:0;padding:0}
html,body{width:1200px;height:2638px;overflow:hidden}
body{position:relative;background:var(--white);font-family:"Open Sans",sans-serif;color:var(--text)}
.abs{position:absolute}

.brand{display:flex;align-items:center;gap:10px;font-family:"Roboto",sans-serif;font-weight:900;color:var(--ink-blue);white-space:nowrap}
.brand .mark{background:var(--ink-blue);border-radius:3px}

.site-header{left:0;top:0;width:1200px;height:90px;background:var(--white)}
.site-header .brand{left:112px;top:22px;font-size:27px}
.site-header .brand .mark{width:26px;height:26px}
.nav{right:0;top:31px;display:flex;font-family:"Open Sans",sans-serif;font-weight:700;font-size:15px;color:var(--text)}
.nav a{position:absolute;color:inherit;text-decoration:none;text-shadow:0 1px 2px rgba(0,0,0,.25);white-space:nowrap}

.hero{left:0;top:90px;width:1200px;height:642px;background:var(--sky)}
.hero-panel{left:83px;top:53px;width:517px;height:534px;background:var(--blue);color:var(--white)}
.hero-panel h1{position:absolute;left:55px;top:140px;font-family:"Roboto",sans-serif;font-weight:700;font-size:45px;line-height:47px;letter-spacing:-.5px}
.hero-panel p{position:absolute;left:55px;top:332px;width:400px;font-size:14.5px;line-height:23px}
.btn-outline{position:absolute;left:150px;top:404px;width:162px;height:41px;border:2px solid var(--white);color:var(--white);font-size:13px;letter-spacing:1.5px;font-weight:600;display:flex;align-items:center;justify-content:center}
.hero-photo{left:600px;top:53px;width:516px;height:534px;background:linear-gradient(135deg,var(--photo-a),var(--photo-b))}

.coaching .brand{left:115px;top:772px;font-size:26px}
.coaching .brand .mark{width:24px;height:24px}
.coaching h2{left:428px;top:762px;font-family:"Roboto",sans-serif;font-weight:700;font-size:45px;color:var(--ink-blue)}
.pill{left:147px;top:857px;width:254px;height:57px;border-radius:29px;background:var(--sky);color:var(--white);font-family:"Roboto",sans-serif;font-weight:700;font-size:24px;display:flex;align-items:center;justify-content:center}

.role{width:240px;text-align:center;top:954px}
.role .icon{width:76px;height:76px;border-radius:50%;background:var(--sky);margin:0 auto;display:flex;align-items:center;justify-content:center}
.role h3{font-family:"Open Sans",sans-serif;font-weight:400;font-size:26px;line-height:33px;margin-top:16px}
.role ul{list-style:none;margin-top:14px;font-family:"Roboto",sans-serif;font-weight:700;font-size:17.5px;line-height:22px;color:var(--ink-blue)}

.story{left:83px;width:1033px;height:158px;border:18px solid var(--blue);border-radius:30px;background:var(--white)}
.story h4{position:absolute;left:62px;top:14px;width:600px;font-family:"Roboto",sans-serif;font-weight:700;font-size:28px;line-height:33px;color:var(--ink-blue)}
.btn-read{position:absolute;left:787px;top:33px;width:128px;height:40px;background:var(--sky);color:var(--white);font-size:15px;display:flex;align-items:center;justify-content:center}

.contact{left:0;top:1760px;width:1200px;height:629px;background:var(--navy);overflow:hidden}
.contact .ghost{position:absolute;left:0;top:220px;width:1200px;text-align:center;font-family:"Roboto",sans-serif;font-weight:900;font-size:170px;color:var(--navy-faint);letter-spacing:6px;white-space:nowrap}
.contact h2{position:absolute;left:0;width:1200px;top:72px;text-align:center;font-family:"Roboto",sans-serif;font-weight:700;font-size:45px;color:var(--white)}
.field{position:absolute;left:384px;width:497px;height:42px;background:var(--white);border:1px solid #cfd6e0;font-size:14px;color:#6b6b6b;padding:11px 11px}
.field.message{height:108px}
.btn-submit{position:absolute;left:384px;top:544px;width:101px;height:40px;background:var(--sky);color:var(--text);font-size:15px;display:flex;align-items:center;justify-content:center}

.site-footer{left:0;top:2389px;width:1200px;height:161px;background:var(--white)}
.site-footer .brand{left:130px;top:46px;font-size:36px}
.site-footer .brand .mark{width:32px;height:32px}
.social{position:absolute;top:29px;width:12px;height:12px;border-radius:50%;background:var(--ink-blue)}
.mini{position:absolute;top:94px;height:43px;border:1px solid #b8b8b8;font-size:14px;color:#6b6b6b;padding:12px 11px}
.mini-submit{position:absolute;left:1011px;top:94px;width:102px;height:42px;background:var(--blue);color:var(--white);font-size:15px;display:flex;align-items:center;justify-content:center}

.legal{left:0;top:2550px;width:1200px;height:88px;background:var(--bar);color:var(--white);font-size:12px;font-weight:600;display:flex;align-items:center;justify-content:center}
.legal a{color:#9fc3ea}
</style>
</head>
<body>

<header class="abs site-header">
  <div class="abs brand"><span class="mark"></span>Pins &amp; Dials</div>
  <nav class="abs nav" style="left:0;width:1200px">
    <a style="left:656px">HOME</a>
    <a style="left:742px">COACH</a>
    <a style="left:835px">CONTACT</a>
    <a style="left:945px">BOOKING</a>
    <a style="left:1056px">BLOG</a>
  </nav>
</header>

<section class="abs hero">
  <div class="abs hero-panel">
    <h1>Pins &amp; Dials - Agile<br>Team Coaching</h1>
    <p>Agile Team Coaching teams working major IT projects, multplue months/years</p>
    <div class="btn-outline">LEARN MORE</div>
  </div>
  <div class="abs hero-photo" role="img" aria-label="Photo of two colleagues reviewing work together on a laptop"></div>
</section>

<section class="coaching">
  <div class="abs brand"><span class="mark"></span>Pins &amp; Dials</div>
  <h2 class="abs">AGILE COACHING</h2>
  <div class="abs pill">The Landscape</div>

  <div class="abs role" style="left:89px">
    <div class="icon"><svg width="40" height="40" viewBox="0 0 40 40" fill="none" stroke="#fff" stroke-width="2"><circle cx="20" cy="20" r="17"/><circle cx="20" cy="16" r="6"/><path d="M9 32c2-6 6-9 11-9s9 3 11 9"/></svg></div>
    <h3>Multiple<br>Teams</h3>
    <ul><li>Development</li><li>Business</li></ul>
  </div>
  <div class="abs role" style="left:349px">
    <div class="icon"><svg width="40" height="40" viewBox="0 0 40 40" fill="none" stroke="#fff" stroke-width="2"><circle cx="20" cy="9" r="4"/><path d="M13 20c1-4 4-6 7-6s6 2 7 6z"/><circle cx="11" cy="24" r="4"/><path d="M4 35c1-4 4-6 7-6s6 2 7 6z"/><circle cx="29" cy="24" r="4"/><path d="M22 35c1-4 4-6 7-6s6 2 7 6z"/></svg></div>
    <h3>Multiple<br>Players</h3>
    <ul><li>Development</li><li>Business</li></ul>
  </div>
  <div class="abs role" style="left:610px">
    <div class="icon"><svg width="40" height="40" viewBox="0 0 40 40" fill="none" stroke="#fff" stroke-width="2"><rect x="13" y="5" width="14" height="30" rx="2"/><line x1="17" y1="9" x2="23" y2="9"/><circle cx="20" cy="31" r="1"/><path d="M9 15c-2 3-2 7 0 10M31 15c2 3 2 7 0 10"/></svg></div>
    <h3>IT</h3>
    <ul><li>Scrum Masters</li><li>Program Managers</li><li>Developers</li><li>Architects</li><li>Integration Specialists</li></ul>
  </div>
  <div class="abs role" style="left:870px">
    <div class="icon"><svg width="40" height="40" viewBox="0 0 40 40" fill="none" stroke="#fff" stroke-width="2"><circle cx="20" cy="16" r="11"/><circle cx="20" cy="16" r="6"/><path d="M13 25l-5 10 5-1 3 4 4-9M27 25l5 10-5-1-3 4-4-9"/></svg></div>
    <h3>Business</h3>
    <ul><li>UAT Testers</li><li>Business Requirements</li><li>Analysts</li><li>Product Owners</li><li>Product Managers</li></ul>
  </div>
</section>

<article class="abs story" style="top:1345px">
  <h4>My role as a technical scrum master and team coach</h4>
  <div class="btn-read">Read More</div>
</article>
<article class="abs story" style="top:1576px">
  <h4>My role as a business transformation program manager and team coach:</h4>
  <div class="btn-read">Read More</div>
</article>

<section class="abs contact">
  <div class="ghost" aria-hidden="true">PINS &amp; DIALS</div>
  <h2>CONTACT US</h2>
  <div class="field" style="top:165px">First Name</div>
  <div class="field" style="top:217px">Second Name</div>
  <div class="field" style="top:269px">Enter a valid email address</div>
  <div class="field" style="top:321px">Enter your phone (e.g. +14155552675)</div>
  <div class="field" style="top:372px">Enter Subject</div>
  <div class="field message" style="top:424px">Enter your message</div>
  <div class="btn-submit">Submit</div>
</section>

<footer class="abs site-footer">
  <div class="abs brand"><span class="mark"></span>Pins &amp; Dials</div>
  <span class="social" style="left:911px"></span>
  <span class="social" style="left:969px"></span>
  <span class="social" style="left:1028px"></span>
  <span class="social" style="left:1087px"></span>
  <div class="mini" style="left:624px;width:180px">Name</div>
  <div class="mini" style="left:817px;width:180px">Email</div>
  <div class="mini-submit">Submit</div>
</footer>

<div class="abs legal"><span><a>Templates</a> created with <a>Website Builder Software</a>.</span></div>

</body>
</html>
```